Business card design needed

I am branching out into the world of private practice in Speech Pathology. My clients will be aged 0-17; the business card will be distributed within my existing teacher and parent networks in schools.

I work with clients to develop their speech, language, literacy, fluency, swallowing and voice. I like to think that parents hand over their money to me because I've offered a fun session with positive outcomes/growth and for an affordable price.

I'm flexible with colours; though think something bright would be ideal. I'm not wanting anything too cutesy or 'little kid'. I'd like for it to stand out in a bulging purse or on a fridge crammed with papers.

Industry/Entity Type

Teacher

Contact Information for Business Card

Wren Hollow Speech Pathology Pty Ltd
Molly Fenwick
Speech Pathologist
Ph: 0419 826 307
Email: mollyfenwick@quillpost.com

Logo Text

Logo styles of interest
Character Logo
Wordmark Logo
Lettermark Logo
Requirements
Must have
• A kind of graphic to represent the core business - that is, providing intervention to children 0-17 with communication needs (e.g., speech, language, literacy, swallowing, voice, fluency)

Should not have
• Pictures of babies or children.
Love hearts.

```html
<!DOCTYPE html>
<html lang="en">
<head>
<meta charset="utf-8">
<title>Wren Hollow Speech Pathology – Business Card</title>
<link rel="stylesheet" href="https://fonts.googleapis.com/css2?family=Open+Sans:wght@400;600&display=swap">
<style>
  :root {
    --backdrop: #1d1d1f;
    --card: #fbfbfb;
    --band-blue: #2b3595;
    --bubble-blue: #1b77bc;
    --name-blue: #1a6db0;
    --quote-navy: #2c2a6b;
    --ink: #1f1f1f;
    --rule: #555555;
    --mark-dot: #e8541e;
    --logo-ink: #2b2b2b;
  }
  * { box-sizing: border-box; margin: 0; padding: 0; }
  html, body {
    width: 1200px; height: 876px; overflow: hidden;
    background: var(--backdrop);
    font-family: "Open Sans", Verdana, sans-serif;
  }
  .stage { position: relative; width: 1200px; height: 876px; }
  .card {
    position: absolute; left: 290px; width: 620px; height: 354px;
    background: var(--card); overflow: hidden;
    box-shadow: 0 10px 30px rgba(0,0,0,.5);
  }
  .card--front { top: 64px; }
  .card--back { top: 458px; }

  /* front */
  .front-band {
    position: absolute; left: 0; right: 0; top: 108px; height: 78px;
    background: var(--band-blue);
  }
  .front-seal {
    position: absolute; left: 210px; top: 22px; width: 200px; height: 200px;
    border-radius: 50%; background: var(--card);
    display: flex; flex-direction: column; align-items: center; justify-content: center; gap: 8px;
  }
  .brand-name {
    color: var(--logo-ink); font-weight: 600; text-align: center;
    text-transform: uppercase; letter-spacing: .04em; line-height: 1.2;
  }
  .front-seal .brand-name { font-size: 17px; }
  .brand-dot { width: 22px; height: 22px; border-radius: 50%; background: var(--mark-dot); }
  .tagline {
    position: absolute; left: 30px; right: 30px; top: 238px;
    color: var(--quote-navy); font-size: 19px; line-height: 1.3; text-align: center;
  }

  /* back */
  .contact-bubble { position: absolute; left: 300px; top: 34px; width: 296px; height: 96px; }
  .contact-list {
    position: absolute; left: 318px; top: 46px; color: #ffffff; font-size: 16px; line-height: 1.55;
    list-style: none;
  }
  .contact-list span { display: inline-block; width: 62px; }
  .person {
    position: absolute; right: 26px; top: 140px; text-align: right; color: var(--ink);
  }
  .person-name { color: var(--name-blue); font-size: 27px; font-weight: 400; margin-bottom: 8px; }
  .person-rule {
    position: absolute; right: 14px; top: 184px; width: 290px; height: 1px; background: var(--rule);
  }
  .person-role, .person-company { font-size: 17px; line-height: 1.45; }
  .person-role { margin-top: 6px; }
  .back-brand {
    position: absolute; left: 28px; top: 178px; width: 250px;
    display: flex; flex-direction: column; align-items: center; gap: 10px;
  }
  .back-brand .brand-name { font-size: 22px; }
  .back-brand .brand-dot { width: 30px; height: 30px; }
</style>
</head>
<body>
<main class="stage">

  <section class="card card--front" aria-label="Card front">
    <div class="front-band"></div>
    <div class="front-seal">
      <div class="brand-dot"></div>
      <div class="brand-name">Wren Hollow<br>Speech Pathology</div>
    </div>
    <p class="tagline">“Providing fun, effective and affordable intervention to support development of speech and language skills in children and adolescents.”</p>
  </section>

  <section class="card card--back" aria-label="Card back">
    <svg class="contact-bubble" viewBox="0 0 296 96" aria-hidden="true">
      <path d="M10 0 H286 Q296 0 296 10 V66 Q296 76 286 76 H166 L154 94 L150 76 H10 Q0 76 0 66 V10 Q0 0 10 0 Z" fill="var(--bubble-blue)"/>
    </svg>
    <ul class="contact-list">
      <li><span>Phone:</span>0419 826 307</li>
      <li><span>Email:</span>mollyfenwick@quillpost.com</li>
    </ul>
    <div class="person-rule"></div>
    <div class="person">
      <h1 class="person-name">Molly Fenwick</h1>
      <p class="person-role">Speech Pathologist</p>
      <p class="person-company">Wren Hollow Speech Pathology Pty Ltd</p>
    </div>
    <div class="back-brand">
      <div class="brand-dot"></div>
      <div class="brand-name">Wren Hollow<br>Speech Pathology</div>
    </div>
  </section>

</main>
</body>
</html>
```